Next-Gen B2B Sales Negotiation App - UI Design for iOS

Develop a user-friendly dark-mode interface for a B2B sales negotiation assistant app for a company called Quorvel. The UI will showcase a single screen with features like counterparty search, agenda selection, and email drafting. Design should reflect a functional iOS app with realistic placeholder data to create a genuine experience.

Precise task description in attachment.

Target Market(s)

B2B

Requirements
Must have
• Each UI picture should look like a screen capture of an iphone
Nice to have
• The UI designs need to show the navigation and the app in use

```html
<!DOCTYPE html>
<html lang="en">
<head>
<meta charset="utf-8">
<title>Quorvel – Negotiation Assistant Screens</title>
<link rel="stylesheet" href="https://fonts.googleapis.com/css2?family=Roboto:wght@400;500;700&family=Exo+2:wght@700&family=Orbitron:wght@500&display=swap">
<style>
:root{
  --board:#76717a;
  --screen:#0b060d;
  --purple:#8c1c92;
  --purple-deep:#4b0f5a;
  --magenta:#c845cf;
  --teal:#0ba3ad;
  --teal-light:#1fc3c9;
  --line:#5d5763;
  --text:#ffffff;
  --muted:#cfc8d3;
  --sig:#c23dd0;
}
*{box-sizing:border-box;margin:0;padding:0}
html,body{width:1200px;height:2244px;overflow:hidden;background:var(--board)}
.board{position:absolute;left:0;top:0;width:1144px;height:2139px;transform:scale(1.049);transform-origin:0 0;font-family:"Roboto",sans-serif;color:var(--text)}
.screen{position:absolute;width:414px;overflow:hidden;background:
  radial-gradient(ellipse 90% 45% at 0% 100%, rgba(150,30,160,.75), transparent 70%),
  radial-gradient(ellipse 70% 35% at 10% 60%, rgba(120,20,130,.35), transparent 75%),
  var(--screen);
  box-shadow:0 20px 60px rgba(0,0,0,.35)}
.abs{position:absolute}
.brand{left:55px;top:28px;font-family:"Exo 2",sans-serif;font-weight:700;font-size:27px;letter-spacing:.5px;color:#f1eef3}
.menu{left:335px;top:29px;width:34px;height:34px;border:2px solid #fff;border-radius:50%}
.menu svg{position:absolute;left:8px;top:9px}
.step{display:flex;align-items:center;gap:12px;left:33px;font-size:19.5px;font-weight:700}
.step .num{width:34px;height:34px;border-radius:50%;background:var(--purple);display:flex;align-items:center;justify-content:center;font-size:14px;font-weight:700}
.party{width:114px;height:114px;border-radius:50%;border:2px solid #55505a;background:#15101a;display:flex;flex-direction:column;align-items:center;justify-content:center;font-size:16.5px;text-align:center;line-height:1.1}
.party.active{background:var(--purple);border-color:#6e5a75}
.party svg{margin-bottom:8px}
.agenda{left:28px;width:360px;height:64px;border-radius:6px;border:2px solid var(--magenta);background:linear-gradient(90deg,#5c0f6c,#8b1e98 55%,#c544cd);display:flex;align-items:center;justify-content:center;gap:28px;font-family:"Orbitron",sans-serif;font-size:36px;letter-spacing:2px}
.box{left:28px;width:360px;border:2px solid var(--line);border-radius:8px}
.method{left:53px;width:310px;height:55px;border-radius:3px;background:linear-gradient(90deg,#86208f,#5a1068);display:flex;align-items:center;gap:14px;padding-left:8px;font-size:20px;font-weight:700;letter-spacing:.3px}
.method .ico{width:37px;height:37px;border-radius:50%;background:#fff;display:flex;align-items:center;justify-content:center}
.picked .name{font-size:29px;font-weight:500}
.picked .role{font-size:25px;color:var(--teal-light);margin-top:6px}
.dim{opacity:.28}
.field{border:1px solid #cfcfcf;border-radius:3px;background:#0b070d;font-size:13px;display:flex;align-items:center;justify-content:space-between;padding:0 18px 0 20px}
.teal-btn{background:var(--teal);border-radius:12px;display:flex;align-items:center;justify-content:center;font-weight:700;color:#fff}
.label{font-size:16px}
.modal{left:20px;top:274px;width:374px;height:450px;border:1px solid #bdbdbd;background:rgba(8,5,10,.82)}
.radio{width:14px;height:14px;border:2px solid #fff;border-radius:50%}
.bullet{display:flex;align-items:center;gap:14px;font-size:17px;left:72px}
.message{left:32px;top:545px;width:354px;height:187px;background:linear-gradient(180deg,#1a0c22,#0a060c);padding:22px 30px 0 33px;font-size:14.5px;line-height:24.5px;color:var(--muted)}
</style>
</head>
<body>
<svg width="0" height="0" style="position:absolute">
  <symbol id="i-menu" viewBox="0 0 16 14"><rect x="0" y="1" width="16" height="2.2" rx="1" fill="#fff"/><rect x="0" y="6" width="16" height="2.2" rx="1" fill="#fff"/><rect x="0" y="11" width="16" height="2.2" rx="1" fill="#fff"/></symbol>
  <symbol id="i-bank" viewBox="0 0 28 26"><path d="M14 0 L28 6 V8 H0 V6 Z" fill="#fff"/><rect x="3" y="10" width="3.5" height="11" fill="#fff"/><rect x="9.5" y="10" width="3.5" height="11" fill="#fff"/><rect x="15.5" y="10" width="3.5" height="11" fill="#fff"/><rect x="21.5" y="10" width="3.5" height="11" fill="#fff"/><rect x="0" y="22" width="28" height="4" fill="#fff"/></symbol>
  <symbol id="i-user" viewBox="0 0 26 30"><circle cx="13" cy="8" r="8" fill="#fff"/><path d="M0 30 C0 20 5 17 13 17 C21 17 26 20 26 30 Z" fill="#fff"/></symbol>
  <symbol id="i-group" viewBox="0 0 38 26"><circle cx="19" cy="6" r="6" fill="#fff"/><circle cx="7" cy="9" r="4.5" fill="#fff"/><circle cx="31" cy="9" r="4.5" fill="#fff"/><path d="M10 26 C10 17 13 14 19 14 C25 14 28 17 28 26 Z" fill="#fff"/><path d="M0 24 C0 17 3 15 7 15 C9 15 10 16 11 17 C9 19 8 21 8 24 Z" fill="#fff"/><path d="M38 24 C38 17 35 15 31 15 C29 15 28 16 27 17 C29 19 30 21 30 24 Z" fill="#fff"/></symbol>
  <symbol id="i-agenda" viewBox="0 0 30 30"><rect x="0" y="3" width="15" height="3.5" fill="#fff"/><rect x="0" y="13" width="22" height="3.5" fill="#fff"/><rect x="0" y="23" width="30" height="3.5" fill="#fff"/></symbol>
  <symbol id="i-mail" viewBox="0 0 18 13"><rect x="0" y="0" width="18" height="13" rx="1.5" fill="#8c1c92"/><path d="M1 1.5 L9 7.5 L17 1.5" stroke="#fff" stroke-width="1.6" fill="none"/></symbol>
  <symbol id="i-share" viewBox="0 0 18 18"><circle cx="4" cy="9" r="3" fill="#8c1c92"/><circle cx="14" cy="3.5" r="3" fill="#8c1c92"/><circle cx="14" cy="14.5" r="3" fill="#8c1c92"/><path d="M4 9 L14 3.5 M4 9 L14 14.5" stroke="#8c1c92" stroke-width="1.8"/></symbol>
  <symbol id="i-phone" viewBox="0 0 20 20"><path d="M4 1 L8 1 L9 6 L6.5 7.5 C7.5 10 10 12.5 12.5 13.5 L14 11 L19 12 L19 16 C19 18 17.5 19 16 19 C8 18.5 1.5 12 1 4 C1 2.5 2 1 4 1 Z" fill="#8c1c92"/></symbol>
  <symbol id="i-search" viewBox="0 0 18 18"><circle cx="7.5" cy="7.5" r="5.5" stroke="#fff" stroke-width="2.6" fill="none"/><path d="M11.5 11.5 L16.5 16.5" stroke="#fff" stroke-width="3" stroke-linecap="round"/></symbol>
  <symbol id="i-caret" viewBox="0 0 8 5"><path d="M0 0 H8 L4 5 Z" fill="#fff"/></symbol>
  <symbol id="i-cal" viewBox="0 0 12 12"><rect x="1" y="2" width="10" height="9" stroke="#fff" stroke-width="1.4" fill="none"/><rect x="1" y="2" width="10" height="2.5" fill="#fff"/><rect x="3" y="0" width="1.5" height="3" fill="#fff"/><rect x="7.5" y="0" width="1.5" height="3" fill="#fff"/></symbol>
  <symbol id="i-chev" viewBox="0 0 10 16"><path d="M2 1 L8.5 8 L2 15" stroke="#1fc3c9" stroke-width="2" fill="none"/></symbol>
  <symbol id="i-cursor" viewBox="0 0 20 24"><path d="M6 1 C7.5 1 8 2 8 3 V10 L9 9.5 C10 9 11 9.5 11.3 10.4 C12.3 9.8 13.4 10.3 13.6 11.2 C14.6 10.7 16 11.2 16 12.6 V17 C16 20 14 23 10.5 23 H9 C7 23 5.5 22 4.5 20.5 L1.5 15.5 C1 14.5 1.6 13.5 2.6 13.5 C3.2 13.5 3.7 13.8 4 14.3 V3 C4 2 4.6 1 6 1 Z" fill="#fff" stroke="#111" stroke-width="1.2"/></symbol>
</svg>

<main class="board">

  <!-- Screen 1: counterparty choice -->
  <section class="screen" style="left:139px;top:104px;height:775px">
    <div class="abs brand">quorvel</div>
    <div class="abs menu"><svg width="14" height="12"><use href="#i-menu"/></svg></div>
    <div class="abs step" style="top:87px"><span class="num">01</span>Select your Counterparty</div>
    <div class="abs party active" style="left:24px;top:142px"><svg width="28" height="26"><use href="#i-bank"/></svg>Company</div>
    <div class="abs party" style="left:150px;top:142px"><svg width="26" height="30"><use href="#i-user"/></svg>Individual</div>
    <div class="abs party" style="left:276px;top:142px"><svg width="36" height="25" style="margin-bottom:4px"><use href="#i-group"/></svg>Group of<br>Individuals</div>
    <div class="abs step" style="top:282px"><span class="num">02</span>Book a Meeting</div>
    <div class="abs agenda" style="top:330px"><svg width="28" height="30"><use href="#i-agenda"/></svg>AGENDA</div>
    <div class="abs step" style="top:410px"><span class="num">03</span>Choose the Contact Method</div>
    <div class="abs box" style="top:462px;height:250px"></div>
    <div class="abs method" style="top:494px"><span class="ico"><svg width="18" height="13"><use href="#i-mail"/></svg></span>EMAIL</div>
    <div class="abs method" style="top:562px"><span class="ico"><svg width="18" height="18"><use href="#i-share"/></svg></span>LINKWAVE</div>
    <div class="abs method" style="top:629px"><span class="ico"><svg width="20" height="20"><use href="#i-phone"/></svg></span>PHONE CALL</div>
  </section>

  <!-- Screen 2: counterparty type dialog -->
  <section class="screen" style="left:591px;top:104px;height:775px">
    <div class="abs brand dim">quorvel</div>
    <div class="abs menu dim"><svg width="14" height="12"><use href="#i-menu"/></svg></div>
    <div class="abs step dim" style="top:87px"><span class="num">01</span>Select your Counterparty</div>
    <div class="abs party active" style="left:24px;top:142px"><svg width="28" height="26"><use href="#i-bank"/></svg>Company</div>
    <div class="abs party dim" style="left:150px;top:142px"><svg width="26" height="30"><use href="#i-user"/></svg>Individual</div>
    <div class="abs party dim" style="left:276px;top:142px"><svg width="36" height="25" style="margin-bottom:4px"><use href="#i-group"/></svg>Group of<br>Individuals</div>
    <svg class="abs" style="left:108px;top:240px" width="22" height="27"><use href="#i-cursor"/></svg>
    <div class="abs modal">
      <div class="abs" style="left:0;right:0;top:38px;text-align:center;font-size:20px;font-weight:500">Select Counterparty Type</div>
      <div class="abs" style="right:14px;top:14px;font-size:22px;font-weight:700">×</div>
      <div class="abs" style="left:26px;top:94px;font-size:14px">Company search</div>
      <div class="abs field" style="left:19px;top:124px;width:335px;height:48px;padding-left:37px;padding-right:42px;font-size:14px">Brightwell Inc<svg width="17" height="17"><use href="#i-search"/></svg></div>
      <div class="abs" style="left:18px;top:193px;width:336px;height:233px;border:1px solid #4c4750"></div>
      <div class="abs" style="left:34px;top:211px;width:92px;height:43px;border-radius:6px;background:#fff;color:#b32a2a;display:flex;align-items:center;justify-content:center;font-size:15px;font-weight:700">Brightwell</div>
      <div class="abs" style="left:139px;top:221px;font-size:17px;font-weight:500">Brightwell Inc</div>
      <div class="abs" style="left:34px;top:269px;font-size:14px">Select Contacted Roles</div>
      <div class="abs field" style="left:33px;top:300px;width:307px;height:47px;padding-left:23px;padding-right:26px">CEO<svg width="8" height="5"><use href="#i-caret"/></svg></div>
      <div class="abs teal-btn" style="left:247px;top:368px;width:92px;height:35px;font-size:12px;border-radius:10px">SUBMIT</div>
    </div>
  </section>

  <!-- Screen 3: meeting booking -->
  <section class="screen" style="left:139px;top:917px;height:1119px">
    <div class="abs brand">quorvel</div>
    <div class="abs menu"><svg width="14" height="12"><use href="#i-menu"/></svg></div>
    <div class="abs step" style="top:86px"><span class="num">01</span>Select your Counterparty</div>
    <div class="abs party active" style="left:36px;top:156px"><svg width="28" height="26"><use href="#i-bank"/></svg>Company</div>
    <div class="abs picked" style="left:178px;top:166px"><div class="name">Brightwell Inc</div><div class="role">CEO</div></div>
    <div class="abs step" style="top:284px"><span class="num">02</span>Book a Meeting</div>
    <div class="abs agenda" style="top:338px"><svg width="28" height="30"><use href="#i-agenda"/></svg>AGENDA</div>
    <svg class="abs" style="left:361px;top:394px" width="22" height="27"><use href="#i-cursor"/></svg>
    <div class="abs box" style="top:424px;height:352px"></div>
    <div class="abs label" style="left:64px;top:459px">Meeting Duration</div>
    <div class="abs field" style="left:200px;top:450px;width:148px;height:41px;justify-content:flex-end"><svg width="8" height="5"><use href="#i-caret"/></svg></div>
    <div class="abs label" style="left:65px;top:514px">Proposed Date</div>
    <div class="abs field" style="left:201px;top:504px;width:148px;height:42px;font-size:12px;padding:0 12px 0 16px">Choose Date<svg width="12" height="12"><use href="#i-cal"/></svg></div>
    <div class="abs radio" style="left:96px;top:580px"></div>
    <div class="abs" style="left:135px;top:578px;font-size:15px">Online</div>
    <div class="abs" style="left:204px;top:578px;width:1px;height:20px;background:#777"></div>
    <div class="abs radio" style="left:230px;top:580px"></div>
    <div class="abs" style="left:269px;top:578px;font-size:15px">On-Site</div>
    <div class="abs teal-btn" style="left:148px;top:625px;width:118px;height:45px;font-size:17px">SUBMIT</div>
    <div class="abs bullet" style="top:693px"><svg width="10" height="16"><use href="#i-chev"/></svg>We can make you more money</div>
    <div class="abs bullet" style="top:723px"><svg width="10" height="16"><use href="#i-chev"/></svg>We can save your time and so on</div>
    <div class="abs step" style="top:786px"><span class="num">03</span>Choose the Contact Method</div>
    <div class="abs box" style="top:836px;height:249px"></div>
    <div class="abs method" style="top:868px"><span class="ico"><svg width="18" height="13"><use href="#i-mail"/></svg></span>EMAIL</div>
    <div class="abs method" style="top:936px"><span class="ico"><svg width="18" height="18"><use href="#i-share"/></svg></span>LINKWAVE</div>
    <div class="abs method" style="top:1003px"><span class="ico"><svg width="20" height="20"><use href="#i-phone"/></svg></span>PHONE CALL</div>
  </section>

  <!-- Screen 4: email draft -->
  <section class="screen" style="left:591px;top:917px;height:956px">
    <div class="abs brand">quorvel</div>
    <div class="abs menu"><svg width="14" height="12"><use href="#i-menu"/></svg></div>
    <div class="abs step" style="top:87px"><span class="num">01</span>Select your Counterparty</div>
    <div class="abs party active" style="left:35px;top:149px"><svg width="28" height="26"><use href="#i-bank"/></svg>Company</div>
    <div class="abs picked" style="left:178px;top:158px"><div class="name">Brightwell Inc</div><div class="role">CEO</div></div>
    <div class="abs step" style="top:271px"><span class="num">02</span>Book a Meeting</div>
    <div class="abs agenda" style="top:318px"><svg width="28" height="30"><use href="#i-agenda"/></svg>AGENDA</div>
    <div class="abs step" style="top:398px"><span class="num">03</span>Choose the Contact Method</div>
    <div class="abs box" style="top:447px;height:86px"></div>
    <div class="abs method" style="top:462px"><span class="ico"><svg width="18" height="13"><use href="#i-mail"/></svg></span>EMAIL</div>
    <svg class="abs" style="left:352px;top:506px" width="22" height="27"><use href="#i-cursor"/></svg>
    <div class="abs message">Hi Marek, I am reaching out to you as I have a solution to save your money and time. I am kindly proposing a meeting for week 8, for instance on Monday 17 February.</div>
    <div class="abs" style="left:65px;top:687px;font-size:14.5px;font-weight:500;color:var(--sig)">-Best regards, Elias</div>
    <div class="abs teal-btn" style="left:280px;top:684px;width:91px;height:35px;font-size:12px;border-radius:12px">SEND NOW</div>
    <div class="abs box" style="top:744px;height:176px"></div>
    <div class="abs method" style="top:771px"><span class="ico"><svg width="18" height="18"><use href="#i-share"/></svg></span>LINKWAVE</div>
    <div class="abs method" style="top:838px"><span class="ico"><svg width="20" height="20"><use href="#i-phone"/></svg></span>PHONE CALL</div>
  </section>

</main>
</body>
</html>
```